Plakat-Design für LACH-TRANCE-ABEND
Zielgruppe
Ich bin Hypnotiseur und trete europaweit bei div. Events mit meiner LACH-TRANCE-ABEND auf (www.lach-trance-abend.example)
Aufgabenstellung
Das Plakat sollte die Elemente Hypnose+Comedy darstellen. Es wird für ein renommiertes Theater gebraucht für deren Leuchtkästen im Format: TIFF/PSD (alternativ JPG) 594mm x 840mm + 1mm Beschnitt.
Das Plakat sollte unten ein freies Störerfeld haben, damit dieses auch für zukünftige Gastspiele genutzt werden kann.
INFOS auf dem Plakat:
-Künstlername (=Varomir)
-Lach-Trance-Abend
-echte Live-Hypnose
Die Show heisst "Träum!" (wie auf einigen Bildern von mir ja dargestellt)
Das Plakat sollte eine gewisse Wertigkeit vermitteln, etwas exklusives, einmaliges. Die Show ist für Erwachsene, daher kein kindliches, zu verspieltes Design. Lieber klar und exklusiv, hochwertig. Danke!

```html
<!DOCTYPE html>
<html lang="de">
<head>
<meta charset="utf-8">
<title>Träum! – Plakat</title>
<link rel="stylesheet" href="https://fonts.googleapis.com/css2?family=Cinzel:wght@400;500&family=Cormorant+Garamond:wght@500&display=swap">
<style>
  :root {
    --stage: #1b1d2a;
    --night: #1e1230;
    --violet: #3a1f56;
    --nebula: #6b3f9a;
    --haze: #f3f1e4;
    --pink-light: #f6d3ea;
    --pink: #d68cc4;
    --text-soft: #d9cfe4;
    --gold: #d9c46a;
  }
  html, body {
    margin: 0;
    width: 1200px;
    height: 797px;
    overflow: hidden;
    background: var(--stage);
  }
  .poster {
    position: absolute;
    left: 346px;
    top: 18px;
    width: 508px;
    height: 760px;
    overflow: hidden;
    background:
      radial-gradient(ellipse 40% 30% at 45% 88%, rgba(107,63,154,.55), transparent 70%),
      radial-gradient(ellipse 55% 35% at 60% 70%, rgba(90,50,140,.45), transparent 70%),
      linear-gradient(180deg, var(--violet) 0%, var(--violet) 55%, var(--night) 100%);
    font-family: "Cinzel", serif;
    color: var(--text-soft);
  }
  .portrait {
    position: absolute;
    left: 0;
    right: 0;
    top: 0;
    height: 600px;
    background:
      radial-gradient(ellipse 38% 42% at 50% 38%, rgba(200,150,160,.85), transparent 75%),
      linear-gradient(180deg, var(--haze) 0%, #e6e0d6 50%, #e6e0d6 100%);
    -webkit-mask-image: linear-gradient(180deg, #000 0%, #000 42%, transparent 100%);
    mask-image: linear-gradient(180deg, #000 0%, #000 42%, transparent 100%);
  }
  .artist {
    position: absolute;
    left: 97px;
    top: 440px;
    margin: 0;
    font-size: 28px;
    font-weight: 400;
    line-height: 1;
    letter-spacing: 2px;
    color: var(--pink-light);
  }
  .show-title {
    position: absolute;
    left: 0;
    right: 0;
    top: 470px;
    margin: 0;
    text-align: center;
    font-size: 108px;
    font-weight: 400;
    line-height: 1.25;
    letter-spacing: 2px;
    background: linear-gradient(180deg, var(--pink-light), var(--pink));
    -webkit-background-clip: text;
    background-clip: text;
    color: transparent;
  }
  .tagline {
    position: absolute;
    left: 0;
    right: 0;
    top: 614px;
    margin: 0;
    text-align: center;
    font-size: 12.5px;
    letter-spacing: 1.5px;
  }
  .pitch {
    position: absolute;
    left: 0;
    right: 0;
    top: 638px;
    margin: 0;
    text-align: center;
    font-family: "Cormorant Garamond", serif;
    font-size: 7.5px;
    line-height: 10px;
    text-transform: uppercase;
    letter-spacing: .5px;
    color: var(--text-soft);
  }
  .brand {
    position: absolute;
    left: 0;
    right: 0;
    top: 688px;
    display: flex;
    justify-content: center;
    align-items: center;
    gap: 5px;
    font-size: 10px;
    color: var(--text-soft);
  }
  .brand-dot {
    width: 9px;
    height: 9px;
    border-radius: 50%;
    background: var(--text-soft);
  }
  .web {
    position: absolute;
    left: 0;
    right: 0;
    top: 724px;
    margin: 0;
    text-align: center;
    font-size: 9.5px;
    letter-spacing: 1px;
    color: var(--gold);
  }
  .booking {
    position: absolute;
    left: 0;
    right: 0;
    top: 746px;
    margin: 0;
    text-align: center;
    font-size: 6.3px;
    letter-spacing: .8px;
    color: var(--text-soft);
  }
</style>
</head>
<body>
  <main class="poster">
    <div class="portrait" role="img" aria-label="Porträtfoto des Hypnotiseurs vor hell überstrahlter Stadtkulisse, mit violettem Sternennebel überlagert"></div>
    <p class="artist">VAROMIR</p>
    <h1 class="show-title">TRÄUM</h1>
    <p class="tagline">LACH-TRANCE-ABEND &nbsp;&nbsp;- ECHTE LIVE-HYPNOSE</p>
    <p class="pitch">Eine einzigartige Show, die Ihre Gäste garantiert nicht vergessen werden!<br>So etwas haben Sie sicherlich noch nicht gesehen und erlebt!<br>Bestes, witziges und unvergessliches Entertainment.</p>
    <div class="brand"><span class="brand-dot"></span><span>Varomir</span></div>
    <p class="web">WWW.LACH-TRANCE-ABEND.EXAMPLE</p>
    <p class="booking">SHOW INFO AND TICKET BOOKING INFO GOES HERE - SHOW INFO AND TICKET BOOKING INFO GOES HERE</p>
  </main>
</body>
</html>
```